Clear tides coaching programme

I need a flyer designed to promote my coaching programme. The programme is designed to help people who are feeling a bit lost in their life, looking for new possiblities or that they want more focus in their goals. It is an intensive programme designed to help people achieve real change in their lives. It is a premium product targeted at senior managers, directors and business leaders. I care passionately about helping people achieve their potential. I would like the design to fit with the logo (attached) and I've drafted the content (also attached). I would like it to be A5 and affordable to print - so not full colour.

```html
<!DOCTYPE html>
<html lang="en">
<head>
<meta charset="utf-8">
<title>Clear Tides Coaching Programme</title>
<link href="https://fonts.googleapis.com/css2?family=Arimo:ital,wght@0,400;0,700;1,400&display=swap" rel="stylesheet">
<style>
  :root {
    --page: #ffffff;
    --band-blue: #3333f0;
    --band-yellow: #ffd633;
    --rule-teal: #33c6c9;
    --title-blue: #1a1ad6;
    --brand-purple: #4b3a8c;
    --brand-teal: #2fb8a8;
    --ink: #111111;
    --link: #1f5fd6;
  }
  * { margin: 0; padding: 0; box-sizing: border-box; }
  html, body { width: 846px; height: 1200px; overflow: hidden; background: var(--page); }
  body { font-family: "Arimo", Arial, sans-serif; color: var(--ink); }
  .flyer { position: relative; width: 846px; height: 1200px; }
  .frame { position: absolute; inset: 0; }
  .title {
    position: absolute; left: 110px; top: 143px; width: 460px;
    text-align: center; color: var(--title-blue);
    font-size: 26px; font-weight: 700; letter-spacing: 3px; line-height: 33px;
  }
  .quote {
    position: absolute; left: 121px; top: 223px; width: 438px;
    font-size: 19.5px; line-height: 25px; font-style: italic; text-align: justify;
  }
  .quote cite { font-style: normal; }
  .brand {
    position: absolute; left: 566px; top: 140px; width: 170px; height: 150px;
    display: flex; flex-direction: column; align-items: center; justify-content: center; gap: 14px;
  }
  .brand-dot { width: 92px; height: 92px; border-radius: 50%; background: var(--brand-teal); }
  .brand-name {
    color: var(--brand-purple); font-size: 21px; font-weight: 400;
    line-height: 24px; text-align: center; text-transform: uppercase;
  }
  .rule { position: absolute; left: 114px; width: 618px; height: 4px; background: var(--rule-teal); }
  .questions {
    position: absolute; left: 120px; top: 343px; width: 600px;
    font-size: 18.5px; line-height: 25px;
  }
  .questions h2 { font-size: 18.5px; font-weight: 700; }
  .questions li { list-style: none; font-style: italic; }
  .details {
    position: absolute; left: 120px; top: 522px; width: 602px;
    font-size: 17px; line-height: 20.5px;
  }
  .details p { margin-bottom: 20.5px; }
  .details p.tight { margin-bottom: 0; }
  .cta {
    position: absolute; left: 120px; top: 962px; width: 607px;
    font-size: 20.5px; line-height: 26px; text-align: justify;
  }
  .cta a { color: var(--link); }
</style>
</head>
<body>
<main class="flyer">
  <svg class="frame" width="846" height="1200" viewBox="0 0 846 1200" aria-hidden="true">
    <polygon points="64,73 98,73 78,1125 64,1125" fill="var(--band-blue)"/>
    <polygon points="98,73 780,73 780,107" fill="var(--band-yellow)"/>
    <polygon points="766,100 780,100 780,1125 752,1125" fill="var(--band-blue)"/>
    <polygon points="64,1089 64,1125 752,1125" fill="var(--band-yellow)"/>
  </svg>

  <h1 class="title">CLEAR TIDES COACHING<br>PROGRAMME</h1>

  <p class="quote">“The secret of change is to focus all of your energy not on fighting the old, but on building the new”. <cite>Theron</cite></p>

  <div class="brand">
    <span class="brand-dot"></span>
    <span class="brand-name">Reaching<br>Further</span>
  </div>

  <div class="rule" style="top:318px"></div>

  <section class="questions">
    <h2>Are you:</h2>
    <ul>
      <li>Fed up but unsure how to move on?</li>
      <li>Finding it hard to focus?</li>
      <li>Dreaming of what could come next in your life?</li>
      <li>Looking for new opportunities and possibilities?</li>
    </ul>
  </section>

  <div class="rule" style="top:494px"></div>

  <section class="details">
    <p>So make that first step towards a <strong>happier life</strong> and take up your own, personally tailored <strong>‘Clear Tides’</strong> coaching journey.</p>
    <p>This programme consists of <strong>6 face to face coaching sessions</strong>, each 90 minutes long and carefully designed around you, your needs and goals. You will also benefit from free email support in between your sessions, development feedback, recommended resources to support your journey and a bespoke action plan.</p>
    <p class="tight">This programme will <strong>help you achieve your goals</strong> and increase your satisfaction with your work and home life.</p>
    <p>&nbsp;Why work with me?</p>
    <p>I’m a coach and transformational leader with a decade of experience in delivering better results for individuals, organisations and customers. I’m passionate about helping people achieve their potential and find new possibilities.</p>
  </section>

  <div class="rule" style="top:944px"></div>

  <p class="cta">So, take the first step today towards your own 'Clear Tides' and book a free 15 minute phone or Vidlink consultation by emailing me at <a href="mailto:hello@reachingfurther.example">hello@reachingfurther.example</a></p>
</main>
</body>
</html>
```